Business Card for staff member of football club SC Brenval

I would like to get a business card template for all staff member of our soccer club.

The card should use as much as possible the 2 colors of the club : Red which is the main color and blue which is the alternative color. It can be balanced between the two like our logo.

I prefer simple and lean design.

Contact Information for Business Card

Bussiness card should have all main stuff as describe here below in must have.

Font styles to use
Sans Serif

Requirements
Must have
• Name : Laurent DESPRATIN
Fonction : Président
Mobile : +41 xx xxx xx xx
Email : first.lastname@scbrenval.ch
Adresse of the club : SC Brenval, 1873 Brenval
Website of the club : www.scbrenval.ch
Nice to have
• Version with and without picture of the staff member

A version for men, a version for women staff member.

```html
<!DOCTYPE html>
<html lang="en">
<head>
<meta charset="utf-8">
<title>SC Brenval – Staff Business Cards</title>
<link rel="stylesheet" href="https://fonts.googleapis.com/css2?family=Questrial&display=swap">
<style>
  :root {
    --club-blue: #228acb;
    --club-red: #ea213e;
    --card-white: #ffffff;
    --ink: #111314;
    --portrait: #050808;
    --bg-centre: #115d87;
    --bg-edge: #2d3e66;
    --text-light: #ffffff;
  }
  * { box-sizing: border-box; margin: 0; padding: 0; }
  html, body { width: 1043px; height: 1200px; overflow: hidden; }
  body {
    position: relative;
    font-family: "Questrial", "Century Gothic", sans-serif;
    background: radial-gradient(ellipse at 50% 55%, var(--bg-centre) 0%, var(--bg-edge) 85%);
    color: var(--text-light);
  }
  .section-title {
    position: absolute;
    left: 0; width: 100%;
    text-align: center;
    font-size: 108px;
    line-height: 1;
    letter-spacing: -1px;
    color: var(--text-light);
  }
  .section-title--front { top: 66px; }
  .section-title--back { top: 748px; }

  .card {
    position: absolute;
    width: 438px; height: 250px;
    background: var(--card-white);
    overflow: hidden;
  }
  .card--blue { --accent: var(--club-blue); }
  .card--red { --accent: var(--club-red); }
  .card__panel { position: absolute; inset: 0; width: 100%; height: 100%; }
  .card__panel polygon { fill: var(--accent); }

  .card__portrait {
    position: absolute;
    left: 12px; top: 48px;
    width: 160px; height: 202px;
    border-radius: 60px 60px 0 0;
    background: linear-gradient(180deg, #111616, var(--portrait));
  }

  .card__identity {
    position: absolute;
    left: 193px; top: 13px;
    width: 218px;
    text-align: center;
  }
  .card__name { font-size: 19px; line-height: 1.2; white-space: nowrap; }
  .card__role {
    display: flex; align-items: center; gap: 5px;
    margin-top: 3px;
    font-size: 15px;
  }
  .card__role::before, .card__role::after {
    content: ""; flex: 1; height: 1.5px; background: var(--text-light);
  }

  .card__contacts {
    position: absolute;
    left: 200px; top: 154px;
    list-style: none;
    font-size: 14.5px;
  }
  .card__contacts li {
    display: flex; align-items: center; gap: 7px;
    height: 21.5px;
    white-space: nowrap;
  }
  .card__contacts svg { width: 16px; height: 16px; flex: none; }

  .club-mark {
    position: absolute;
    display: flex; flex-direction: column; align-items: center;
    color: var(--ink);
  }
  .club-mark__dot { border-radius: 50%; background: var(--club-red); }
  .club-mark__name { white-space: nowrap; }
  .card .club-mark { left: 14px; top: 70px; width: 116px; gap: 12px; }
  .card .club-mark__dot { width: 54px; height: 54px; }
  .card .club-mark__name { font-size: 20px; }

  .card--back .club-mark { left: 0; top: 48px; width: 100%; gap: 18px; }
  .card--back .club-mark__dot { width: 96px; height: 96px; }
  .card--back .club-mark__name { font-size: 32px; }
</style>
</head>
<body>
<svg width="0" height="0" style="position:absolute">
  <defs>
    <symbol id="icon-phone" viewBox="0 0 16 16">
      <rect x="0" y="0" width="16" height="16" rx="3" fill="#fff"/>
      <path d="M4.2 3.2l2 .2.8 2.4-1.2 1c.6 1.3 1.6 2.3 2.9 2.9l1-1.2 2.4.8.2 2c-.3.6-.9 1-1.6.9C7.2 11.9 4.1 8.8 3.3 5c-.1-.8.3-1.5.9-1.8z" fill="#111"/>
    </symbol>
    <symbol id="icon-mail" viewBox="0 0 16 16">
      <rect x="1" y="3" width="14" height="10" fill="none" stroke="#fff" stroke-width="1.2"/>
      <path d="M1 3l7 6 7-6M1 13l5-5M15 13l-5-5" fill="none" stroke="#fff" stroke-width="1"/>
    </symbol>
    <symbol id="icon-web" viewBox="0 0 16 16">
      <rect x="0" y="0" width="16" height="16" rx="2" fill="#fff"/>
      <path d="M5 2.5v10l2.4-2.2 1.8 3.6 1.6-.8-1.8-3.5h3.2z" fill="#111"/>
    </symbol>
    <symbol id="icon-pin" viewBox="0 0 16 16">
      <rect x="0" y="0" width="16" height="16" rx="2" fill="#fff"/>
      <path d="M8 2a4.2 4.2 0 00-4.2 4.2C3.8 9.4 8 14 8 14s4.2-4.6 4.2-7.8A4.2 4.2 0 008 2z" fill="#111"/>
      <circle cx="8" cy="6.2" r="1.7" fill="#fff"/>
    </symbol>
  </defs>
</svg>

<h1 class="section-title section-title--front">Front</h1>

<!-- Blue card, club name -->
<article class="card card--blue" style="left:69px; top:194px;">
  <svg class="card__panel" viewBox="0 0 438 250" aria-hidden="true"><polygon points="128,0 438,0 438,250 128,250 209,120"/></svg>
  <div class="club-mark"><span class="club-mark__dot"></span><span class="club-mark__name">SC Brenval</span></div>
  <div class="card__identity"><p class="card__name">Laurent DESPRATIN</p><p class="card__role">President</p></div>
  <ul class="card__contacts">
    <li><svg><use href="#icon-phone"/></svg>+41 xx xxx xx xx</li>
    <li><svg><use href="#icon-mail"/></svg>first.lastname@scbrenval.ch</li>
    <li><svg><use href="#icon-web"/></svg>www.scbrenval.ch</li>
    <li><svg><use href="#icon-pin"/></svg>SC Brenval, 1873 Brenval</li>
  </ul>
</article>

<!-- Blue card, portrait -->
<article class="card card--blue" style="left:549px; top:194px;">
  <div class="card__portrait" role="img" aria-label="Portrait photo of the staff member (man)"></div>
  <svg class="card__panel" viewBox="0 0 438 250" aria-hidden="true"><polygon points="128,0 438,0 438,250 128,250 209,120"/></svg>
  <div class="card__identity"><p class="card__name">Laurent DESPRATIN</p><p class="card__role">President</p></div>
  <ul class="card__contacts">
    <li><svg><use href="#icon-phone"/></svg>+41 xx xxx xx xx</li>
    <li><svg><use href="#icon-mail"/></svg>first.lastname@scbrenval.ch</li>
    <li><svg><use href="#icon-web"/></svg>www.scbrenval.ch</li>
    <li><svg><use href="#icon-pin"/></svg>SC Brenval, 1873 Brenval</li>
  </ul>
</article>

<!-- Red card, club name -->
<article class="card card--red" style="left:61px; top:482px;">
  <svg class="card__panel" viewBox="0 0 438 250" aria-hidden="true"><polygon points="128,0 438,0 438,250 128,250 209,120"/></svg>
  <div class="club-mark"><span class="club-mark__dot"></span><span class="club-mark__name">SC Brenval</span></div>
  <div class="card__identity"><p class="card__name">Laurent DESPRATIN</p><p class="card__role">President</p></div>
  <ul class="card__contacts">
    <li><svg><use href="#icon-phone"/></svg>+41 xx xxx xx xx</li>
    <li><svg><use href="#icon-mail"/></svg>first.lastname@scbrenval.ch</li>
    <li><svg><use href="#icon-web"/></svg>www.scbrenval.ch</li>
    <li><svg><use href="#icon-pin"/></svg>SC Brenval, 1873 Brenval</li>
  </ul>
</article>

<!-- Red card, portrait -->
<article class="card card--red" style="left:552px; top:482px;">
  <div class="card__portrait" role="img" aria-label="Portrait photo of the staff member (woman)"></div>
  <svg class="card__panel" viewBox="0 0 438 250" aria-hidden="true"><polygon points="128,0 438,0 438,250 128,250 209,120"/></svg>
  <div class="card__identity"><p class="card__name">Laurent DESPRATIN</p><p class="card__role">President</p></div>
  <ul class="card__contacts">
    <li><svg><use href="#icon-phone"/></svg>+41 xx xxx xx xx</li>
    <li><svg><use href="#icon-mail"/></svg>first.lastname@scbrenval.ch</li>
    <li><svg><use href="#icon-web"/></svg>www.scbrenval.ch</li>
    <li><svg><use href="#icon-pin"/></svg>SC Brenval, 1873 Brenval</li>
  </ul>
</article>

<h1 class="section-title section-title--back">Back</h1>

<article class="card card--back" style="left:289px; top:872px; height:251px;">
  <div class="club-mark"><span class="club-mark__dot"></span><span class="club-mark__name">SC Brenval</span></div>
</article>
</body>
</html>
```